Tradeshwo display 8x10 high resolution backdrop

I created a backdrop I wanted to use via Chat GPT but the image isn't high quality enough for print so I want someone to recreate it as close as possible to my creation. See attached, TY!

```html
<!DOCTYPE html>
<html lang="en">
<head>
<meta charset="utf-8">
<title>NFS Trade Show Backdrop</title>
<link href="https://fonts.googleapis.com/css2?family=Oswald:wght@400;500;600;700&family=Montserrat:wght@400;500&display=swap" rel="stylesheet">
<style>
:root{
  --navy:#151a5c;
  --navy-deep:#0c0f24;
  --royal:#1f3fa0;
  --bright:#1a6fc4;
  --sky:#3d8fe0;
  --ink:#111111;
  --white:#ffffff;
  --bg:#e6e7e9;
  --rule:#d9dbe0;
}
*{margin:0;padding:0;box-sizing:border-box}
html,body{width:1200px;height:1200px;overflow:hidden;background:var(--bg)}
body{position:relative;font-family:"Montserrat",sans-serif}
.backdrop{position:absolute;left:0;top:120px;width:1200px;height:960px;background:var(--white);overflow:hidden}
.abs{position:absolute}

.brand{left:50px;top:92px;display:flex;align-items:center;gap:14px}
.brand-dot{width:58px;height:58px;border-radius:50%;background:var(--royal)}
.brand-name{font-family:"Oswald",sans-serif;font-weight:700;font-size:64px;line-height:1;color:var(--royal);letter-spacing:1px}
.brand-sub{left:50px;top:165px;font-family:"Oswald",sans-serif;font-weight:600;font-size:12px;color:var(--ink);letter-spacing:.3px}

.pillars{left:366px;top:86px;display:flex}
.pillar{width:86px;height:112px;border-left:1px solid #555;display:flex;flex-direction:column;align-items:center}
.pillar svg{width:48px;height:48px;margin-top:4px}
.pillar span{margin-top:16px;font-family:"Oswald",sans-serif;font-weight:500;font-size:13px;line-height:1.45;text-align:center;color:var(--ink)}

.head-1{left:60px;top:232px;font-family:"Oswald",sans-serif;font-weight:700;font-size:66px;color:var(--ink);letter-spacing:.5px}
.head-2{left:56px;top:298px;font-family:"Oswald",sans-serif;font-weight:700;font-size:84px;letter-spacing:.5px;
  background:linear-gradient(180deg,#1f5dc2 0%,#1a2a86 100%);-webkit-background-clip:text;background-clip:text;color:transparent}
.tagline{left:58px;top:408px;width:714px;display:flex;align-items:center;gap:18px}
.tagline i{flex:1;height:3px;background:var(--royal)}
.tagline span{font-family:"Oswald",sans-serif;font-weight:500;font-size:17px;letter-spacing:5px;color:var(--ink)}

.band{left:0;top:446px;width:780px;height:49px;background:linear-gradient(90deg,#1a56ab,#1b3c98 60%,#1b2f8a);
  clip-path:polygon(0 0,97.5% 0,100% 50%,97.5% 100%,0 100%);
  display:flex;align-items:center;padding-left:59px;font-family:"Oswald",sans-serif;font-weight:500;font-size:18.5px;letter-spacing:4.3px;color:var(--white)}

.products{left:47px;top:521px;display:flex}
.product{width:137.5px;height:237px;border-left:1px solid var(--rule);display:flex;flex-direction:column;align-items:center;text-align:center;padding:0 4px}
.product-shot{width:110px;height:110px;margin-top:12px;border-radius:12px;background:radial-gradient(circle at 45% 40%,#6fa6ea,#2a56b8 60%,#d9dde6 100%)}
.product h3{margin-top:28px;font-family:"Oswald",sans-serif;font-weight:500;font-size:13px;white-space:nowrap;color:var(--royal)}
.product p{margin-top:6px;font-size:9.2px;line-height:1.5;color:#222}

.panels{left:880px;top:316px;width:320px;height:446px}
.tile{position:absolute;left:0;width:320px;height:110px;display:flex;align-items:center;
  background:linear-gradient(100deg,#11164f 0%,#1c2380 55%,#2c34a8 100%);
  clip-path:polygon(0 50%,22px 0,100% 0,100% 100%,22px 100%)}
.tile svg{position:absolute;left:40px;top:27px;width:56px;height:56px}
.tile span{margin-left:128px;font-family:"Oswald",sans-serif;font-weight:500;font-size:18px;line-height:24px;color:var(--white);white-space:nowrap}

.footer-pin{left:50px;top:867px;width:40px;height:40px;border-radius:50%;background:var(--white);display:flex;align-items:center;justify-content:center}
.footer-serv{left:100px;top:858px;color:var(--white)}
.footer-serv b{display:block;font-family:"Oswald",sans-serif;font-weight:600;font-size:19px}
.footer-serv em{display:block;font-style:normal;font-family:"Oswald",sans-serif;font-weight:400;font-size:14px;letter-spacing:.2px}
.footer-rule{top:857px;width:1px;height:46px;background:#9aa0b8}
.footer-web{left:451px;top:870px;width:370px;text-align:center;font-family:"Oswald",sans-serif;font-weight:500;font-size:24px;color:var(--white);letter-spacing:1px}
.footer-web span{color:#2f63d6}
.footer-motto{left:888px;top:856px;color:var(--white)}
.footer-motto small{display:block;font-family:"Oswald",sans-serif;font-size:13.5px}
.footer-motto strong{display:block;font-family:"Oswald",sans-serif;font-weight:600;font-size:24.5px;letter-spacing:.3px}
</style>
</head>
<body>
<div class="backdrop">

  <svg class="abs" style="left:0;top:0" width="1200" height="960" viewBox="0 0 1200 960">
    <defs>
      <linearGradient id="sceneTone" x1="0" y1="0" x2="0" y2="1">
        <stop offset="0" stop-color="#5e8cc4"/>
        <stop offset=".35" stop-color="#b9c8dc"/>
        <stop offset=".52" stop-color="#e6b46a"/>
        <stop offset=".62" stop-color="#3f6f9a"/>
        <stop offset="1" stop-color="#2b5c93"/>
      </linearGradient>
      <linearGradient id="footTone" x1="0" y1="0" x2="0" y2="1">
        <stop offset="0" stop-color="#2a66c4"/>
        <stop offset=".25" stop-color="#0f1a44"/>
        <stop offset="1" stop-color="#0b0e1f"/>
      </linearGradient>
    </defs>
    <path d="M676,0 C720,150 780,330 900,460" fill="none" stroke="#d6e6f8" stroke-width="12"/>
    <path d="M700,0 C745,150 800,300 900,420" fill="none" stroke="#2f7fd8" stroke-width="7"/>
    <path d="M712,0 C755,140 810,260 900,360 L900,316 C830,240 790,130 752,0 Z" fill="#172a8a"/>
    <svg x="0" y="0" width="1200" height="320" role="img" aria-label="Photo of a water treatment plant with clarifier tanks at sunset">
      <path d="M750,0 C790,130 830,240 881,316 L1200,316 L1200,0 Z" fill="url(#sceneTone)"/>
    </svg>
    <path d="M0,790 C200,775 400,815 650,808 C880,800 1050,775 1200,770 L1200,960 L0,960 Z" fill="url(#footTone)"/>
    <path d="M0,790 C200,775 400,815 650,808 C880,800 1050,775 1200,770" fill="none" stroke="#5aa0f0" stroke-width="2" opacity=".7"/>
  </svg>

  <div class="abs brand"><div class="brand-dot"></div><div class="brand-name">NFS</div></div>
  <div class="abs brand-sub">Northgate Flow Systems</div>

  <div class="abs pillars">
    <div class="pillar">
      <svg viewBox="0 0 48 48" fill="none" stroke="#1f3fa0" stroke-width="2"><circle cx="24" cy="19" r="14"/><circle cx="24" cy="19" r="9"/><path d="M24 13l2 4 4 .5-3 3 .8 4-3.8-2-3.8 2 .8-4-3-3 4-.5z"/><path d="M14 29l-6 12 7-2 3 6 5-11M34 29l6 12-7-2-3 6-5-11"/></svg>
      <span>QUALITY<br>BRANDS</span>
    </div>
    <div class="pillar">
      <svg viewBox="0 0 48 48" fill="none" stroke="#1f3fa0" stroke-width="2"><circle cx="24" cy="24" r="8"/><path d="M24 4v7M24 37v7M4 24h7M37 24h7M10 10l5 5M33 33l5 5M38 10l-5 5M15 33l-5 5"/><circle cx="24" cy="24" r="15"/></svg>
      <span>ENGINEERED<br>SOLUTIONS</span>
    </div>
    <div class="pillar">
      <svg viewBox="0 0 48 48" fill="none" stroke="#1f3fa0" stroke-width="2"><path d="M9 26v-4a15 15 0 0 1 30 0v4"/><rect x="6" y="24" width="6" height="11" rx="2"/><rect x="36" y="24" width="6" height="11" rx="2"/><path d="M39 35c0 5-6 8-12 8"/><circle cx="24" cy="25" r="5"/></svg>
      <span>EXPERT<br>SUPPORT</span>
    </div>
    <div class="pillar">
      <svg viewBox="0 0 48 48" fill="none" stroke="#1f3fa0" stroke-width="2"><path d="M3 14l8-2 6 16-6 3zM45 14l-8-2-6 16 6 3z"/><path d="M11 28l9 8c2 2 4 1 5-1l6-7M17 16l6-3 8 3M23 13l-6 6c-1 2 1 3 3 2l5-3"/></svg>
      <span>TURNKEY<br>DELIVERY</span>
    </div>
  </div>

  <div class="abs head-1">SOLUTIONS THAT</div>
  <div class="abs head-2">KEEP WATER MOVING</div>
  <div class="abs tagline"><i></i><span>EXPERTISE. RELIABILITY. RESULTS.</span><i></i></div>
  <div class="abs band">COMPLETE SOLUTIONS FOR THE WATER &amp; WASTEWATER INDUSTRY</div>

  <div class="abs products">
    <div class="product"><div class="product-shot" role="img" aria-label="Split case centrifugal pump"></div><h3>PUMPS</h3><p>Industry leading pumps built for performance, efficiency &amp; reliability.</p></div>
    <div class="product"><div class="product-shot" role="img" aria-label="Electric motor"></div><h3>MOTORS</h3><p>High efficiency motors engineered for durability and long life.</p></div>
    <div class="product"><div class="product-shot" role="img" aria-label="Positive displacement blower"></div><h3>BLOWERS</h3><p>Aerion PD positive displacement blowers for reliable, energy efficient performance.</p></div>
    <div class="product"><div class="product-shot" role="img" aria-label="Variable frequency drive cabinet"></div><h3>VFD &amp; CONTROLS</h3><p>Precision control and energy savings through advanced VFD solutions.</p></div>
    <div class="product"><div class="product-shot" role="img" aria-label="Automatic control valve"></div><h3>AUTOMATION &amp; VALVES</h3><p>Smart automation and reliable valves for optimized system performance.</p></div>
    <div class="product"><div class="product-shot" role="img" aria-label="Skid mounted booster pump system"></div><h3>TURNKEY SOLUTIONS</h3><p>Complete systems designed, integrated and supported by NFS.</p></div>
  </div>

  <div class="abs panels">
    <div class="tile" style="top:0">
      <svg viewBox="0 0 56 56" fill="#fff"><path d="M20 8c-7 10-11 16-11 21a11 11 0 0 0 22 0c0-5-4-11-11-21z"/><path d="M38 18c-8 11-13 18-13 24a13 13 0 0 0 26 0c0-6-5-13-13-24z"/></svg>
      <span>WATER &amp;<br>WASTEWATER<br>EXPERTISE</span>
    </div>
    <div class="tile" style="top:112px">
      <svg viewBox="0 0 56 56" fill="none" stroke="#fff" stroke-width="3.5"><path d="M28 5l-19 7v14c0 12 8 20 19 25 11-5 19-13 19-25v-14z"/><path d="M19 28l7 7 12-13"/></svg>
      <span>TRUSTED<br>PRODUCTS</span>
    </div>
    <div class="tile" style="top:224px">
      <svg viewBox="0 0 56 56" fill="none" stroke="#fff" stroke-width="3.5"><path d="M8 26a20 18 0 1 1 12 17l-10 5 3-9a18 18 0 0 1-5-13z"/><circle cx="20" cy="26" r="1.5" fill="#fff"/><circle cx="28" cy="26" r="1.5" fill="#fff"/><circle cx="36" cy="26" r="1.5" fill="#fff"/></svg>
      <span>LOCAL SUPPORT<br>YOU CAN COUNT ON</span>
    </div>
    <div class="tile" style="top:336px">
      <svg viewBox="0 0 56 56" fill="#fff"><rect x="10" y="26" width="7" height="12"/><rect x="20" y="20" width="7" height="18"/><rect x="30" y="14" width="7" height="24"/><path d="M40 4l6 8h-4v26h-5V12h-4z"/><path d="M6 46c10 5 22 5 34-2l6-4" fill="none" stroke="#fff" stroke-width="3"/></svg>
      <span>BUILT FOR<br>PERFORMANCE.<br>FOCUSED ON<br>YOUR SUCCESS.</span>
    </div>
  </div>

  <div class="abs footer-pin">
    <svg width="20" height="24" viewBox="0 0 20 24"><path d="M10 1a8 8 0 0 0-8 8c0 6 8 14 8 14s8-8 8-14a8 8 0 0 0-8-8z" fill="#1f3fa0"/><circle cx="10" cy="9" r="3" fill="#fff"/></svg>
  </div>
  <div class="abs footer-serv"><b>SERVICING</b><em>VIRGINIA | NORTH CAROLINA | MARYLAND | DELAWARE</em></div>
  <div class="abs footer-rule" style="left:457px"></div>
  <div class="abs footer-web">www.<span>nfs-flowsupply</span>.com</div>
  <div class="abs footer-rule" style="left:840px"></div>
  <div class="abs footer-motto"><small>YOUR PARTNER FOR</small><strong>A BETTER FLOW FORWARD</strong></div>
</div>
</body>
</html>
```